Property Developer - Simple yet Sophisticated and Sharp Business Card

We are a medium sized property developer involved mainly in townhouse developments and land subdivisions.

The company is looking for a simple, sharp and sophisticated business card that will be given to contractors, land owners, financiers etc and thus will need to look professional.

Property development related graphics and art can be used, however the card is not to be too "busy" or crowded. Our company name is KL Estates which could possibly be incorporated into the graphics or artwork.

Single sided and/or double sided designs will be acceptable.

A Simple, Sophisticated, Sharp design please!

Good Luck !

```html
<!DOCTYPE html>
<html lang="en">
<head>
<meta charset="utf-8">
<title>KL Estates – Business Card</title>
<link rel="stylesheet" href="https://fonts.googleapis.com/css2?family=Open+Sans:wght@400;600;700&display=swap">
<style>
  :root {
    --stage: #cfcfcf;
    --card: #ffffff;
    --card-shade: #ececec;
    --card-edge: #a9a9a9;
    --brand-blue: #2a72c9;
    --ink-blue: #2f6fc4;
    --white: #ffffff;
  }
  html, body {
    margin: 0;
    padding: 0;
    width: 1200px;
    height: 1006px;
    overflow: hidden;
    background: var(--stage);
    font-family: "Open Sans", Verdana, Arial, sans-serif;
  }
  .stage {
    position: relative;
    width: 1200px;
    height: 1006px;
  }
  .card {
    position: absolute;
    top: 222px;
    width: 396px;
    height: 590px;
    background: radial-gradient(ellipse at 55% 52%, var(--card) 0%, var(--card) 35%, var(--card-shade) 100%);
    border: 1px solid var(--card-edge);
    box-sizing: border-box;
    overflow: hidden;
  }
  .card--back { left: 177px; }
  .card--front { left: 616px; }

  .brand-band {
    position: absolute;
    left: 118px;
    right: 0;
    top: 364px;
    height: 88px;
    background: var(--brand-blue);
  }
  .brand-mark {
    position: absolute;
    left: 116px;
    top: 362px;
    width: 92px;
    height: 92px;
  }
  .brand-name {
    position: absolute;
    left: 212px;
    top: 420px;
    color: var(--white);
    font-weight: 700;
    font-size: 26px;
    line-height: 1;
    white-space: nowrap;
  }

  .contact-list {
    position: absolute;
    left: 0;
    right: 0;
    top: 478px;
    margin: 0;
    padding: 0;
    list-style: none;
    text-align: center;
    color: var(--ink-blue);
    font-weight: 600;
    font-size: 15px;
    letter-spacing: 1.2px;
    line-height: 19.5px;
  }

  .person {
    position: absolute;
    right: 8px;
    top: 462px;
    text-align: right;
    color: var(--ink-blue);
    font-weight: 600;
    font-size: 21px;
    letter-spacing: 1.5px;
    line-height: 27px;
  }
  .person__name, .person__role { display: block; }
</style>
</head>
<body>
<main class="stage">

  <section class="card card--back" aria-label="Card back with contact details">
    <div class="brand-band"></div>
    <svg class="brand-mark" viewBox="0 0 92 92" aria-hidden="true">
      <circle cx="46" cy="46" r="44" fill="var(--brand-blue)"/>
      <circle cx="46" cy="46" r="39" fill="none" stroke="var(--white)" stroke-width="4"/>
    </svg>
    <span class="brand-name">KL Estates</span>
    <ul class="contact-list">
      <li>P: (07) 3245 8810</li>
      <li>F: (07) 3245 8811</li>
      <li>E: projects@klestates-mail.com</li>
      <li>A: PO Box 2715</li>
      <li>Parkview North QLD 4120</li>
    </ul>
  </section>

  <section class="card card--front" aria-label="Card front with name and title">
    <div class="brand-band"></div>
    <svg class="brand-mark" viewBox="0 0 92 92" aria-hidden="true">
      <circle cx="46" cy="46" r="44" fill="var(--brand-blue)"/>
      <circle cx="46" cy="46" r="39" fill="none" stroke="var(--white)" stroke-width="4"/>
    </svg>
    <span class="brand-name">KL Estates</span>
    <p class="person">
      <span class="person__name">Dana Whitfield</span>
      <span class="person__role">Manager</span>
    </p>
  </section>

</main>
</body>
</html>
```